Furniture retail store requires in store display board design.

I am launching a new bed buying concept in my retail stores and require a point of sale graphic to explain the purchase process to consumers.
1.Select base style.(Including headboard) + 2. Customise legs and storage options. + 3.Choose Colours. + 4. Add your perfect mattress. = Your perfect nights sleep.
I'm imagining a sketchy/whiteboard/chalkboard type effect. The main boards will hang above a bed and will be 150cm wide x 35cm high.
Consumers 30yo+
Retail

```html
<!DOCTYPE html>
<html lang="en">
<head>
<meta charset="UTF-8">
<title>Bed Buying Steps – Display Board</title>
<link rel="stylesheet" href="https://fonts.googleapis.com/css2?family=Indie+Flower&family=Schoolbell&display=swap">
<style>
  :root {
    --board-dark: #1c1c1c;
    --board-mid: #2f2f2f;
    --board-light: #474747;
    --chalk: #f1f1ef;
    --chalk-soft: rgba(241, 241, 239, 0.16);
  }
  html, body {
    margin: 0;
    padding: 0;
    width: 1200px;
    height: 280px;
    overflow: hidden;
    background: var(--board-dark);
  }
  .board {
    position: relative;
    width: 1200px;
    height: 280px;
    overflow: hidden;
    color: var(--chalk);
    background:
      radial-gradient(ellipse 420px 160px at 260px 60px, var(--board-light), transparent 70%),
      radial-gradient(ellipse 380px 150px at 900px 90px, #3e3e3e, transparent 70%),
      radial-gradient(ellipse 500px 140px at 600px 260px, #383838, transparent 70%),
      linear-gradient(180deg, var(--board-mid) 0%, var(--board-dark) 100%);
  }
  .step {
    position: absolute;
    font-family: "Indie Flower", cursive;
    font-size: 25px;
    line-height: 38px;
    text-align: center;
    white-space: nowrap;
    margin: 0;
  }
  .step--base { left: 95px; top: 34px; width: 290px; }
  .step--legs { left: 400px; top: 34px; width: 260px; }
  .step--colours { left: 700px; top: 53px; width: 200px; }
  .step--mattress { left: 975px; top: 34px; width: 170px; }
  .operator {
    position: absolute;
    font-family: "Indie Flower", cursive;
    font-size: 34px;
    line-height: 1;
  }
  .operator--plus-1 { left: 369px; top: 52px; }
  .operator--plus-2 { left: 667px; top: 52px; }
  .operator--plus-3 { left: 921px; top: 52px; }
  .operator--equals { left: 588px; top: 124px; }
  .result {
    position: absolute;
    left: 0;
    top: 150px;
    width: 1200px;
    margin: 0;
    text-align: center;
    font-family: "Schoolbell", cursive;
    font-weight: 400;
    font-size: 64px;
    line-height: 84px;
    letter-spacing: 1px;
  }
  .flourish {
    position: absolute;
    top: 138px;
    width: 215px;
    height: 112px;
    border-radius: 40px;
    background: radial-gradient(ellipse at center, var(--chalk-soft), transparent 72%);
  }
  .flourish--left { left: 20px; }
  .flourish--right { right: 20px; }
</style>
</head>
<body>
  <main class="board">
    <p class="step step--base">Select base style<br>(Including headboard)</p>
    <span class="operator operator--plus-1">+</span>
    <p class="step step--legs">Customise legs and<br>storage options</p>
    <span class="operator operator--plus-2">+</span>
    <p class="step step--colours">Choose Colours</p>
    <span class="operator operator--plus-3">+</span>
    <p class="step step--mattress">Add your<br>perfect mattress</p>
    <span class="operator operator--equals">=</span>

    <div class="flourish flourish--left" role="img" aria-label="Decorative chalk scroll flourish"></div>
    <h1 class="result">Your perfect nights sleep</h1>
    <div class="flourish flourish--right" role="img" aria-label="Decorative chalk scroll flourish"></div>
  </main>
</body>
</html>
```